Bright Locker Haven - Free Moving Truck Design

Looking to wrap graphic on 17' box moving truck for my self storage facility based in orange, california. The graphic will need to cover the 4 sides of the box truck, 2 doors and hood. The design should incorporate our business, but must have a wow, look at me factor. The bulk of our customers are residential, live within 5 miles, have disposable income or have an unexpected need to store personal items. We have several commercial accounts, which tend to be our long term customer, which benefits our business. Our facility features: Free Move-In Truck, Individual door alarms, Coded gate access, Month to Month leases, Senior/Military Discounts, Moving & Packing Supplies, knowledgeable & friendly staff. The truck is intended to be a moving billboard when in use.
website: https://www.brightlockerhaven.example/self-storage/ca/orange/dunmore-ave/

Target Market(s)

Apartment dwellers, residential renters, inventory type businesses such as pharmacuticals, construction, plumbing, HVAC, street vendors, home remodelers, college students,

Industry/Entity Type

Self Storage

Colors
FFF300
FFF600
FEFA6F
FFFEC7
FFFEE8
EB3D1F
EC4F4E
F09395
F8D3D4
FCEDEE

Requirements
Must have
• Logo, "We sell boxes", tie in to our Self Storage business, features, phone number 714-555-0147, email address: brightlockerhavenorange.example, address: 517 W. Dunmore Ave., Orange, Ca 82841
Nice to have
• Real people, row of self storage units
Should not have
• Small font, scriptive font

```html
<!DOCTYPE html>
<html lang="en">
<head>
<meta charset="utf-8">
<title>Bright Locker Haven – Truck Side Wrap</title>
<link rel="stylesheet" href="https://fonts.googleapis.com/css2?family=Archivo+Black&family=Oswald:wght@700&family=Raleway:wght@600;800&display=swap">
<style>
  :root{
    --page-grey:#b3b3b3;
    --brand-yellow:#FFF300;
    --soft-yellow:#FEFA6F;
    --brand-red:#EB3D1F;
    --deep-red:#5c0f07;
    --ink:#1a1a1a;
    --white:#ffffff;
  }
  html,body{margin:0;padding:0;overflow:hidden;}
  body{
    width:939px;height:1200px;
    background:var(--page-grey);
    position:relative;
  }
  .truck-wrap{
    position:absolute;
    left:40px;top:385px;
    width:860px;height:429px;
    box-shadow:0 6px 18px rgba(0,0,0,.35);
  }
  .truck-wrap svg{display:block;width:100%;height:100%;}
  .brand-name{font-family:"Raleway",sans-serif;font-weight:800;fill:var(--brand-yellow);}
  .location{font-family:"Raleway",sans-serif;font-weight:800;fill:var(--brand-red);paint-order:stroke;stroke:var(--white);stroke-width:5px;}
  .address{font-family:"Raleway",sans-serif;font-weight:600;fill:var(--ink);paint-order:stroke;stroke:var(--white);stroke-width:3px;}
  .feature{font-family:"Raleway",sans-serif;font-weight:600;fill:var(--ink);font-size:22px;}
  .bullet{fill:var(--brand-red);}
  .phone{font-family:"Oswald",sans-serif;font-weight:700;fill:var(--white);}
  .website{font-family:"Raleway",sans-serif;font-weight:600;fill:var(--brand-red);}
  .headline{font-family:"Archivo Black",sans-serif;fill:var(--brand-yellow);}
</style>
</head>
<body>
<div class="truck-wrap">
<svg viewBox="0 0 1382 690" xmlns="http://www.w3.org/2000/svg">
  <defs>
    <linearGradient id="unitsTone" x1="0" y1="0" x2="1" y2="0">
      <stop offset="0" stop-color="#ef6a3e"/>
      <stop offset="0.45" stop-color="#f6a57f"/>
      <stop offset="0.8" stop-color="#fde9b0"/>
      <stop offset="1" stop-color="#FFF300"/>
    </linearGradient>
    <linearGradient id="bandTone" x1="0" y1="0" x2="0" y2="1">
      <stop offset="0" stop-color="#EB3D1F"/>
      <stop offset="0.45" stop-color="#e0381b"/>
      <stop offset="1" stop-color="#5c0f07"/>
    </linearGradient>
    <linearGradient id="peopleTone" x1="0" y1="0" x2="0" y2="1">
      <stop offset="0" stop-color="#e8b99a"/>
      <stop offset="0.55" stop-color="#3b6fbf"/>
      <stop offset="1" stop-color="#c89868"/>
    </linearGradient>
    <filter id="headlineShadow" x="-5%" y="-20%" width="110%" height="140%">
      <feDropShadow dx="3" dy="4" stdDeviation="2" flood-color="#3a0a04" flood-opacity=".85"/>
    </filter>
  </defs>

  <!-- background: storage unit row -->
  <rect class="units-photo" role="img" aria-label="Photo of a row of self storage units with roll-up doors, tinted orange" x="0" y="0" width="1382" height="460" fill="url(#unitsTone)"/>

  <!-- right info panel -->
  <rect class="info-panel" x="920" y="0" width="462" height="460" fill="var(--brand-yellow)"/>
  <polygon class="corner-band" points="968,0 1382,0 1382,34 985,34" fill="var(--brand-red)"/>

  <!-- smiling couple with moving box -->
  <rect class="people-photo" role="img" aria-label="Photo of a smiling young couple holding a cardboard moving box and a tape gun" x="415" y="18" width="560" height="442" rx="40" fill="url(#peopleTone)" opacity=".85"/>

  <!-- brand name -->
  <text class="brand-name" font-size="66">
    <tspan x="72" y="110">Bright</tspan>
    <tspan x="72" y="178">Locker</tspan>
    <tspan x="72" y="246">Haven</tspan>
  </text>
  <text class="location" x="72" y="308" font-size="52">Orange</text>
  <text class="address" font-size="19">
    <tspan x="74" y="342">517 W. Dunmore Ave.,</tspan>
    <tspan x="74" y="368">Orange, Ca 82841</tspan>
  </text>

  <!-- features -->
  <g class="feature-list">
    <rect class="bullet" x="996" y="64" width="14" height="14"/><text class="feature" x="1018" y="79">Free Move-In Truck</text>
    <rect class="bullet" x="996" y="97" width="14" height="14"/><text class="feature" x="1018" y="112">Individual door alarms</text>
    <rect class="bullet" x="996" y="130" width="14" height="14"/><text class="feature" x="1018" y="145">Coded gate access</text>
    <rect class="bullet" x="996" y="163" width="14" height="14"/><text class="feature" x="1018" y="178">Month to Month leases</text>
    <rect class="bullet" x="996" y="196" width="14" height="14"/><text class="feature" x="1018" y="211">Senior/Military Discounts</text>
    <rect class="bullet" x="996" y="229" width="14" height="14"/><text class="feature" x="1018" y="244">Moving &amp; Packing Supplies</text>
    <rect class="bullet" x="996" y="262" width="14" height="14"/><text class="feature" x="1018" y="277">knowledgeable &amp; friendly staff</text>
  </g>

  <!-- phone band -->
  <rect class="phone-band" x="922" y="297" width="460" height="98" fill="var(--brand-red)"/>
  <text class="phone" x="1158" y="375" font-size="72" text-anchor="middle">714-555-0147</text>

  <text class="website" x="1158" y="452" font-size="22" text-anchor="middle">www.brightlockerhaven.example</text>

  <!-- bottom headline band -->
  <rect class="headline-band" x="0" y="460" width="1382" height="230" fill="url(#bandTone)"/>
  <text class="headline" x="691" y="552" font-size="84" text-anchor="middle" filter="url(#headlineShadow)">BRIGHT LOCKER HAVEN</text>
</svg>
</div>
</body>
</html>
```